Mendwell47 Business Card Redesign

I want to create a design for brand new business cards, I need something exceptional for clear plastic business card design. Please do not submit without it being on a clear design. Photos of the various logo versions attached.

```html
<!DOCTYPE html>
<html lang="en">
<head>
<meta charset="utf-8">
<title>Mendwell47 Business Card</title>
<link rel="stylesheet" href="https://fonts.googleapis.com/css2?family=Open+Sans:wght@400;600;700&display=swap">
<style>
  :root {
    --backdrop: #d9d3ca;
    --card-top: #efe8da;
    --card-top-light: #e4e6ea;
    --navy: #1d2f5a;
    --navy-deep: #0d121c;
    --navy-glow: #4a6494;
    --gold: #c9993f;
    --gold-light: #ddb565;
    --gold-deep: #8a5e22;
    --ink-light: #eef0f3;
  }
  * { margin: 0; padding: 0; box-sizing: border-box; }
  html, body { width: 1200px; height: 927px; overflow: hidden; }
  body {
    background: var(--backdrop);
    font-family: "Open Sans", sans-serif;
    position: relative;
  }
  .card {
    position: absolute;
    left: 150px; top: 214px;
    width: 896px; height: 500px;
    border-radius: 3px;
    overflow: hidden;
    box-shadow: 0 10px 30px rgba(0,0,0,0.18);
  }
  .card-top {
    position: absolute; left: 0; top: 0; right: 0; height: 210px;
    background: linear-gradient(100deg, var(--card-top) 0%, var(--card-top-light) 35%, var(--card-top) 70%, #e9ddc8 100%);
  }
  .brand-name {
    position: absolute; left: 0; right: 0; top: 62px;
    text-align: center;
    font-weight: 600;
    font-size: 78px;
    letter-spacing: 2px;
    color: var(--gold);
    line-height: 1;
  }
  .card-band {
    position: absolute; left: 0; top: 210px; right: 0; bottom: 0;
    background:
      radial-gradient(ellipse 260px 120px at 150px 0, rgba(74,100,148,0.75), transparent 70%),
      linear-gradient(180deg, var(--navy) 0%, var(--navy-deep) 100%);
  }
  .band-accent {
    position: absolute; top: 210px; right: 0; bottom: 0; width: 330px;
    background: linear-gradient(90deg, rgba(201,153,63,0) 0%, var(--gold-light) 30%, var(--gold) 65%, var(--gold-deep) 100%);
  }
  .contact {
    position: absolute; left: 53px; top: 262px;
  }
  .person-name {
    font-weight: 700; font-size: 30px; letter-spacing: 0.5px;
    color: var(--gold); line-height: 1.2;
  }
  .person-role {
    font-size: 24px; color: var(--ink-light); margin-top: 4px;
  }
  .details { list-style: none; margin-top: 24px; }
  .details li {
    display: flex; align-items: center; gap: 8px;
    font-size: 24px; color: var(--gold); line-height: 32px;
  }
  .details svg { width: 19px; height: 19px; flex: none; }
</style>
</head>
<body>
  <div class="card">
    <div class="card-top"></div>
    <div class="brand-name">MENDWELL47</div>
    <div class="card-band"></div>
    <div class="band-accent"></div>

    <div class="contact">
      <div class="person-name">DANIEL HARPER</div>
      <div class="person-role">Managing Director</div>
      <ul class="details">
        <li>
          <svg viewBox="0 0 20 20" aria-hidden="true"><path fill="#c9993f" d="M2 7c0-2 3-3 8-3s8 1 8 3v2h-4V7H6v2H2z M5 10h10l2 7H3z"/></svg>
          044-555 210 384
        </li>
        <li>
          <svg viewBox="0 0 20 20" aria-hidden="true"><path fill="none" stroke="#c9993f" stroke-width="2" d="M2 8l8-5 8 5v9H2z M2 8l8 6 8-6"/></svg>
          info@mendwell47.com
        </li>
        <li>
          <svg viewBox="0 0 20 20" aria-hidden="true"><circle cx="10" cy="10" r="8.5" fill="#c9993f"/><path fill="#0d121c" d="M6 5c2 0 3 1 2 3s-3 1-3 3-2 0-2-1 1-4 3-5z M12 11c2 0 3 1 2 3s-2 3-3 2 0-2 1-5z"/></svg>
          www.mendwell47.com
        </li>
      </ul>
    </div>
  </div>
</body>
</html>
```